FLYER POSTCARD ADVERT FOR GARNET QUARTER

OUR COMPANY NAME IS TOLVEK DESIGNS.

WE NEED TO MAKE A POSTCARD FRONT AND BACK TO HAND OUT AND MAIL TO LOCAL JEWELERS DESCRIBING OUR WEDDING RING MANUFACTURING AND FINISHING SERVICES.
KEY POINTS WE WOULD LIKE LISTED:

FAST AND RELIABLE CONTRACTORS THAT ARE IN THE WEDDING RING INDUSTRY SINCE 1979

WE OFFER:
SWISS CUTTING
BASIC TO COMPLEX FINISHES AND DESIGNS
HAND CHASING/EMBOSSING AND ENGRAVING
LASER ENGRAVING
DIAMOND SETTING

CUTTING AND FINISHING AS LOW AS $10 PER PIECE

10K - 14K - 18K - PLATINUM - PALLADIUM - .935 SILVER
VOLUME AND SPECIAL ORDERS ACCEPTED
NO MINIMUMS

EMAIL : INFO@TOLVEKDESIGNS.EXAMPLE
TEL: 555 - 314- 9072

Target Market(s)

WHOLESALE JEWELERS

Industry/Entity Type

Jewelry

Font styles to use
Serif

Colors

Designer to choose colors to be used in the design.

Requirements
Must have
• OUR LOGO, WEVE ATTACHED BOTH WHITE AND BLACK BACKGROUND TO USE DEPENDING ON THE COLOR SCHEME.
• ALSO NEEDS THESE KEY POINTS LISTED TOO:
• FAST AND RELIABLE CONTRACTORS AND MANUFACTURERS SERVICING THE WEDDING RING INDUSTRY SINCE 1979
• WE OFFER:
• SWISS CUTTING
• BASIC TO COMPLEX FINISHES AND DESIGNS
• HAND CHASING/EMBOSSING AND ENGRAVING
• LASER ENGRAVING
• DIAMOND SETTING
• CUTTING AND FINISHING AS LOW AS $10 PER PIECE
• 10K - 14K - 18K - PLATINUM - PALLADIUM - .935 SILVER
• VOLUME AND SPECIAL ORDERS ACCEPTED
• NO MINIMUMS
• EMAIL : INFO@TOLVEKDESIGNS.EXAMPLE
• TEL: 555 - 314- 9072
Should not have
• WE DONT MIND COLOR, BUT WE DONT WANT AN EXPLOSION OF COLORS EITHER. WE WOULD LIKE IT TO BE EASY ON THE EYE.

```html
<!DOCTYPE html>
<html lang="en">
<head>
<meta charset="utf-8">
<title>Tolvek Designs – Postcard</title>
<link rel="stylesheet" href="https://fonts.googleapis.com/css2?family=Cinzel:wght@400;600&family=Libre+Baskerville&family=Quicksand:wght@400&family=Hind:wght@300;400;600&display=swap">
<style>
  :root{
    --ink:#2a2a2a;
    --ink-soft:#4a4a4b;
    --gold:#f2b705;
    --gold-deep:#e59c07;
    --gold-text:#f0b20a;
    --paper:#ffffff;
    --muted:#c9c9c9;
    --stage:#e9e6e2;
    --line:#cfcfcf;
  }
  *{margin:0;padding:0;box-sizing:border-box}
  html,body{width:1200px;height:1200px;overflow:hidden;background:var(--stage)}
  .stage{position:relative;width:1200px;height:1200px}
  .card-slot{position:absolute;left:238px;width:724px;height:470px;box-shadow:0 6px 18px rgba(0,0,0,.25)}
  .card-slot--front{top:96px}
  .card-slot--back{top:634px}
  .card{position:absolute;left:0;top:0;width:905px;height:587px;transform:scale(.8);transform-origin:0 0;background:var(--ink);overflow:hidden;font-family:"Hind",sans-serif;color:#fff}
  .card__shapes{position:absolute;inset:0;width:905px;height:587px}
  .abs{position:absolute}

  .brand{display:flex;flex-direction:column;align-items:center;color:var(--gold-text);font-family:"Cinzel",serif;font-weight:400}
  .brand__mark{width:46px;height:46px;border:3px solid var(--gold-text);border-radius:50%;margin-bottom:14px}
  .brand__name{font-size:38px;letter-spacing:2px;line-height:1}
  .brand__sub{font-size:13px;letter-spacing:15px;margin-top:4px;margin-right:-15px}

  .phone{right:32px;top:27px;display:flex;align-items:center;gap:8px;color:var(--gold-text);font-weight:600;font-size:22px}
  .phone svg{width:26px;height:26px}

  .tagline{left:35px;top:228px;width:325px;border-top:1px solid #555;border-bottom:1px solid #555;padding:10px 0 12px}
  .tagline__lead{font-family:"Libre Baskerville",serif;font-size:30px;color:#d8d8d8;line-height:1.2}
  .tagline__key{font-family:"Cinzel",serif;font-weight:600;font-size:46px;color:var(--gold-text);line-height:1.1;letter-spacing:1px}

  .pitch{left:35px;top:460px}
  .pitch__head{font-family:"Quicksand",sans-serif;font-size:28px;color:var(--gold-text);line-height:1.1}
  .pitch__sub{font-size:16px;color:#fff}
  .pitch__sub b{font-weight:600}

  .contact{left:35px;top:536px;display:flex;align-items:center;gap:10px;font-size:15px;color:#fff}
  .contact svg{width:22px;height:16px}
  .contact__gap{width:2px}

  .photo{position:absolute}
  .photo--rings{left:375px;top:115px;width:510px;height:420px;border-radius:50%;background:radial-gradient(ellipse at 35% 45%,#d9c98a 0%,#b9a15a 35%,rgba(200,200,205,.9) 60%,rgba(43,43,43,0) 72%)}
  .photo--thumbs{left:32px;top:322px;width:320px;height:95px;border-radius:40px;background:linear-gradient(90deg,#bdbdbd,#eeeeee 50%,#bdbdbd)}

  .offer{left:35px;top:30px}
  .offer__title{font-family:"Libre Baskerville",serif;font-size:18px;color:var(--gold-text);letter-spacing:1px;margin-bottom:10px}
  .offer__list{list-style:none}
  .offer__list li{position:relative;display:block;padding-left:30px;font-size:15.5px;font-weight:300;color:#dcdcdc;line-height:27.7px;height:27.7px;white-space:nowrap}
  .offer__list li::before{content:"";position:absolute;left:0;top:7px;width:13px;height:13px;border:2px solid var(--gold-text);border-radius:50%}
  .hl{color:var(--gold-text)}

  .contact-title{left:35px;top:498px;font-family:"Libre Baskerville",serif;font-size:23px;color:var(--gold-text)}

  .brand--back{left:585px;top:40px}
  .brand--back .brand__mark{width:36px;height:36px;margin-bottom:10px}
  .brand--back .brand__name{font-size:26px}
  .brand--back .brand__sub{font-size:9px;letter-spacing:10px;margin-right:-10px}

  .stamp{left:776px;top:28px;width:100px;height:109px;border:1px solid var(--line)}
  .address-line{height:1px;background:var(--line);right:30px}
</style>
</head>
<body>
<main class="stage">

  <!-- Front -->
  <section class="card-slot card-slot--front">
    <div class="card card--front">
      <svg class="card__shapes" viewBox="0 0 905 587" aria-hidden="true">
        <path d="M290 0 L365 0 C330 90 330 200 380 300 L400 330 C330 240 300 120 290 0Z" fill="var(--gold)"/>
        <rect x="675" y="25" width="230" height="33" fill="#3a3a3a"/>
        <path d="M0 420 C150 360 330 370 430 420 C600 500 760 480 905 425 L905 587 L0 587Z" fill="var(--gold)"/>
        <path d="M0 430 C150 375 330 385 430 432 C600 508 760 490 905 438 L905 587 L0 587Z" fill="var(--paper)"/>
        <path d="M0 445 C150 395 330 405 430 448 C600 520 760 505 905 455 L905 587 L0 587Z" fill="var(--ink-soft)"/>
      </svg>

      <div class="brand abs" style="left:45px;top:50px">
        <span class="brand__mark"></span>
        <span class="brand__name">TOLVEK</span>
        <span class="brand__sub">DESIGNS</span>
      </div>

      <div class="phone abs">
        <svg viewBox="0 0 26 26"><circle cx="13" cy="13" r="11.5" fill="none" stroke="var(--gold-text)" stroke-width="1.6"/><path d="M9 7.5c1-.6 1.6 0 2 1l.8 1.8c.3.7-.3 1.2-.8 1.6.6 1.5 1.6 2.6 3.1 3.2.4-.5.9-1.1 1.6-.8l1.8.8c1 .4 1.5 1 .9 2-1 1.6-3 1.5-5 .3-2.200-1.3-3.600-3-4.400-5.100-.6-1.900-.7-3.600 0-4.800z" fill="var(--gold-text)"/></svg>
        <span>555 - 314- 9072</span>
      </div>

      <div class="tagline abs">
        <p class="tagline__lead">We specialize in</p>
        <p class="tagline__key">ELEGANCE</p>
      </div>

      <div class="photo photo--rings" role="img" aria-label="Photo of a brushed gold wedding band beside an engraved white gold band"></div>

      <div class="pitch abs">
        <p class="pitch__head">Fast and reliable contractors</p>
        <p class="pitch__sub">that are <b>in the wedding ring industry</b>&nbsp; <b>SINCE 1979</b></p>
      </div>

      <div class="contact abs">
        <svg viewBox="0 0 22 16"><path d="M0 5h5M1 8h4M0 11h5" stroke="var(--gold-text)" stroke-width="1.2"/><rect x="7" y="2" width="14" height="12" fill="none" stroke="var(--gold-text)" stroke-width="1.4"/><path d="M7 2l7 6 7-6" fill="none" stroke="var(--gold-text)" stroke-width="1.4"/></svg>
        <span>info@tolvekdesigns.example</span>
        <span class="contact__gap"></span>
        <svg viewBox="0 0 16 16" style="width:18px"><circle cx="8" cy="8" r="7" fill="none" stroke="var(--gold-text)" stroke-width="1.3"/><ellipse cx="8" cy="8" rx="3" ry="7" fill="none" stroke="var(--gold-text)" stroke-width="1.1"/><path d="M1 8h14M2.5 4.5h11M2.5 11.5h11" stroke="var(--gold-text)" stroke-width="1"/></svg>
        <span>www.tolvekdesigns.example</span>
      </div>
    </div>
  </section>

  <!-- Back -->
  <section class="card-slot card-slot--back">
    <div class="card card--back">
      <svg class="card__shapes" viewBox="0 0 905 587" aria-hidden="true">
        <path d="M450 0 L530 0 C525 210 430 380 300 450 L270 450 C400 370 470 200 450 0Z" fill="var(--gold)"/>
        <path d="M515 0 L905 0 L905 587 L300 587 L300 450 C450 360 520 200 515 0Z" fill="var(--paper)"/>
        <path d="M0 445 C120 420 240 425 330 445 C520 500 760 510 905 465 L905 587 L0 587Z" fill="var(--gold)"/>
        <path d="M0 460 C120 437 240 440 330 458 C520 512 760 522 905 478 L905 587 L0 587Z" fill="var(--paper)"/>
        <path d="M0 472 C120 450 240 455 330 472 C520 525 760 535 905 492 L905 587 L0 587Z" fill="var(--ink-soft)"/>
      </svg>

      <div class="offer abs">
        <h2 class="offer__title">WE OFFER:</h2>
        <ul class="offer__list">
          <li>Swiss cutting</li>
          <li>Basic to complex finishes and designs</li>
          <li>Hand chasing/embossing and engraving</li>
          <li>Laser engraving</li>
          <li>Diamond setting</li>
          <li>Cutting and finishing as low as <span class="hl">$10 per</span> piece</li>
          <li><span class="hl">10k - 14k - 18k</span> - platinum - palladium - <span class="hl">.935</span> silver</li>
          <li>Volume and special orders accepted</li>
          <li>No minimums</li>
        </ul>
      </div>

      <div class="photo photo--thumbs" role="img" aria-label="Photo of four white metal wedding bands with different finishes"></div>

      <div class="brand brand--back abs">
        <span class="brand__mark"></span>
        <span class="brand__name">TOLVEK</span>
        <span class="brand__sub">DESIGNS</span>
      </div>
      <div class="stamp abs"></div>
      <div class="address-line abs" style="top:197px;left:555px"></div>
      <div class="address-line abs" style="top:250px;left:532px"></div>
      <div class="address-line abs" style="top:298px;left:510px"></div>
      <div class="address-line abs" style="top:350px;left:480px"></div>

      <h2 class="contact-title abs">Contact Details :</h2>
      <div class="contact abs" style="top:538px">
        <svg viewBox="0 0 22 16"><path d="M0 5h5M1 8h4M0 11h5" stroke="var(--gold-text)" stroke-width="1.2"/><rect x="7" y="2" width="14" height="12" fill="none" stroke="var(--gold-text)" stroke-width="1.4"/><path d="M7 2l7 6 7-6" fill="none" stroke="var(--gold-text)" stroke-width="1.4"/></svg>
        <span>info@tolvekdesigns.example</span>
        <span class="contact__gap"></span>
        <svg viewBox="0 0 16 16" style="width:18px"><circle cx="8" cy="8" r="7" fill="none" stroke="var(--gold-text)" stroke-width="1.3"/><ellipse cx="8" cy="8" rx="3" ry="7" fill="none" stroke="var(--gold-text)" stroke-width="1.1"/><path d="M1 8h14M2.5 4.5h11M2.5 11.5h11" stroke="var(--gold-text)" stroke-width="1"/></svg>
        <span>www.tolvekdesigns.example</span>
      </div>
    </div>
  </section>

</main>
</body>
</html>
```